Flyer für selbstständigen Finanzierungsvermittler  für Baufinanzierungen
Flyer für selbstständigen Finanzierungsvermittler für Baufinanzierungen
Zielgruppe
seit 1999 selbstständiger Finanzierungsvermittler für Baufinanzierungen.
ich arbeite für (nicht angestellt) ein Maklerbüro in Schorndorf, hier wurde vor Jahren ein Flyer konzepiert.
Zukünftiger Flyer soll von Immobilienmaklern Interessenten ausgehändigt oder in Kundenmappe VEK-Maklerbüro beigelegt werden.
Aufgabenstellung
- der beigefügte Flyer von Lukas Brandel hat schon sehr viel von dem, was ich mir das vorstelle
- die Farben des Maklerbüros sind Blau und weiß, kann aber auch ganz anders entworfen werden
- Es soll ein DinA 4 Flyer werden, ebenso die PDF-Datei hierzu
- Adressfeld: Stefan Kurlen, Baufinanzierungsspezialist, Bankkaufmann, Haldenweg 17, 73814 Halmstetten, Mobil 0171 546 7183, stefan@kurlen48.de
Text für den Flyer, anlehnend an beileigende:
- Längjährige Erfahrung
- Vergleich von über 300 Banken
- Top Konditionen, bis zu 40 Jahre Zinsbindung
- Beratung vor Ort, auch per Viseo und Telefon möglich
- rasche Zusage, aufgrund persönlichem Kontakt zu Entscheidungsträgern der Bank
mitgelieferte Bilder dürfen natürlich zugeschnitten werden (nur bis Brust) oder weniger Hintergrund, etc.

```html
<!DOCTYPE html>
<html lang="de">
<head>
<meta charset="utf-8">
<title>Stefan Kurlen – Baufinanzierung</title>
<link href="https://fonts.googleapis.com/css2?family=Montserrat:wght@700&family=Open+Sans:wght@700&family=Arimo:wght@400&display=swap" rel="stylesheet">
<style>
  :root {
    --bg-dark: #3b3b3b;
    --bg-darker: #343434;
    --paper: #ffffff;
    --brand-blue: #1c6fc2;
    --line-blue: #2b6db3;
    --tick-blue: #2aa4e0;
    --text-light: #ffffff;
  }
  html, body { margin: 0; padding: 0; overflow: hidden; background: var(--bg-dark); }
  .flyer {
    position: relative;
    width: 851px; height: 1200px;
    overflow: hidden;
    background: var(--bg-dark);
    font-family: "Arimo", Arial, sans-serif;
    color: var(--text-light);
  }
  .backdrop { position: absolute; inset: 0; }
  .portrait { position: absolute; left: 0; top: 160px; }
  .name {
    position: absolute; top: 78px; left: 0; width: 836px;
    margin: 0; text-align: center;
    font-family: "Montserrat", sans-serif; font-weight: 700;
    font-size: 49px; letter-spacing: -1px;
    color: var(--brand-blue);
  }
  .role {
    position: absolute; top: 398px; left: 400px; width: 402px;
    margin: 0; text-align: center;
    font-family: "Open Sans", sans-serif; font-weight: 700;
    font-size: 18px; line-height: 30px; letter-spacing: 1.2px;
  }
  .contact {
    position: absolute; top: 505px; right: 51px;
    margin: 0; text-align: right; font-style: normal;
    font-size: 22px; line-height: 33.5px;
  }
  .benefits {
    position: absolute; top: 672px; left: 68px;
    margin: 0; padding: 0; list-style: none;
    font-size: 23px; line-height: 29px;
  }
  .benefits li { display: flex; align-items: flex-start; margin-bottom: 52px; }
  .benefits li:nth-child(2),
  .benefits li:nth-child(3),
  .benefits li:nth-child(4) { margin-bottom: 56px; }
  .tick { flex: none; width: 38px; height: 30px; margin-right: 8px; }
</style>
</head>
<body>
<main class="flyer">
  <svg class="backdrop" width="851" height="1200" viewBox="0 0 851 1200" aria-hidden="true">
    <polygon points="258,0 851,0 851,56 300,462 0,490 0,188" fill="var(--paper)"/>
    <polygon points="0,490 370,566 851,922 851,1200 0,1200" fill="var(--bg-darker)"/>
    <polyline points="0,490 370,566 851,922" fill="none" stroke="var(--line-blue)" stroke-width="1.5"/>
    <line x1="0" y1="1075" x2="180" y2="1200" stroke="var(--line-blue)" stroke-width="1.5"/>
  </svg>

  <svg class="portrait" width="300" height="395" viewBox="0 0 300 395" role="img" aria-label="Porträtfoto von Stefan Kurlen im dunklen Sakko und hellblauem Hemd, bis zur Brust">
    <defs>
      <linearGradient id="portraitTone" x1="0" y1="0" x2="0" y2="1">
        <stop offset="0" stop-color="#c9b3a3"/>
        <stop offset="0.45" stop-color="#8f8f98"/>
        <stop offset="1" stop-color="#2a2c33"/>
      </linearGradient>
    </defs>
    <path d="M95,0 H205 V150 L295,190 L300,388 L0,328 L0,200 L95,150 Z" fill="url(#portraitTone)"/>
  </svg>

  <h1 class="name">STEFAN KURLEN</h1>

  <p class="role">IHR BAUFINANZIERUNGSSPEZIALIST<br>BANKKAUFMANN</p>

  <address class="contact">
    Haldenweg 17, 73814 Halmstetten<br>
    Mobil 0171 546 7183<br>
    stefan@kurlen48.de
  </address>

  <ul class="benefits">
    <li><svg class="tick" viewBox="0 0 38 30" aria-hidden="true"><path d="M3,16 L13,26 L35,3" fill="none" stroke="var(--tick-blue)" stroke-width="5" stroke-linecap="round" stroke-linejoin="round"/></svg>Längjährige Erfahrung</li>
    <li><svg class="tick" viewBox="0 0 38 30" aria-hidden="true"><path d="M3,16 L13,26 L35,3" fill="none" stroke="var(--tick-blue)" stroke-width="5" stroke-linecap="round" stroke-linejoin="round"/></svg>Vergleich von über 300 Banken</li>
    <li><svg class="tick" viewBox="0 0 38 30" aria-hidden="true"><path d="M3,16 L13,26 L35,3" fill="none" stroke="var(--tick-blue)" stroke-width="5" stroke-linecap="round" stroke-linejoin="round"/></svg>Top Konditionen, bis zu 40 Jahre Zinsbindung</li>
    <li><svg class="tick" viewBox="0 0 38 30" aria-hidden="true"><path d="M3,16 L13,26 L35,3" fill="none" stroke="var(--tick-blue)" stroke-width="5" stroke-linecap="round" stroke-linejoin="round"/></svg>Beratung vor Ort, auch per Video und Telefon möglich</li>
    <li><svg class="tick" viewBox="0 0 38 30" aria-hidden="true"><path d="M3,16 L13,26 L35,3" fill="none" stroke="var(--tick-blue)" stroke-width="5" stroke-linecap="round" stroke-linejoin="round"/></svg><span>Rasche Zusage, aufgrund persönlichem Kontakt zu<br>Entscheidungsträgern der Bank</span></li>
  </ul>
</main>
</body>
</html>
```